Dental Business Card Design w/logo

Classic, elegant w/a touch of contemporary
Upscale dental facility located in Modesto CA
Specializing in restorative & general dentistry
Providing exceptional customer service to the community
Updates

I prefer script and not bold writing
If you can use the phone; fax and email icons instead of spelling them out, it would be great
No bold colors
Classy and elegant
In the back of the card I would like to see something like this
Your Next Appointment:
Mon     Tue    Wed    Thur (a box next to each of them for marking)
Date:_______________ at_____________ AM    PM  (a box next to them for marking)

Thank you

Target Market(s)

Well established professional

Industry/Entity Type

Dental

Contact Information for Business Card

Velorine Tamsuki DMD
4176 Larchmont Rd
Suite D7
Modesto, CA 95368

Office: 209-731-5092
Fax: 209-731-8247
Email: tamsukidmd@brivelmail.test

Requirements
Must have
• Unique classic logo
An easily repeatable design that can be used on letterhead and envelopes
Nice to have
• My initials incorporated into unique design
Should not have
• No cartoons or cheesy themes. This is a practice for the well established and professional individual.

```html
<!DOCTYPE html>
<html lang="en">
<head>
<meta charset="utf-8">
<title>Velorine Tamsuki DMD – Business Card, Front and Back</title>
<link rel="stylesheet" href="https://fonts.googleapis.com/css2?family=Parisienne&family=Dancing+Script:wght@400;500&display=swap">
<style>
  :root {
    --page: #f3f1ee;
    --card: #e9ddd0;
    --band-pink: #e391a7;
    --band-plum: #9d5077;
    --ink: #2b2b5c;
    --ink-soft: #1f1f3a;
    --cream: #f4e6dc;
    --disc: #ececea;
    --box-fill: #f2eadf;
    --box-line: #cdb99b;
  }
  html, body {
    margin: 0;
    width: 1200px;
    height: 1200px;
    overflow: hidden;
    background: var(--page);
  }
  .card {
    position: absolute;
    left: 150px;
    width: 900px;
    height: 514px;
    background: var(--card);
    box-shadow: 0 6px 18px rgba(0,0,0,0.12);
    overflow: hidden;
  }
  .card--back { top: 50px; }
  .card--front { top: 636px; }

  .band-left {
    position: absolute;
    left: 0; top: 0;
    width: 150px; height: 100%;
    background: var(--band-pink);
  }
  .band-left .brand {
    position: absolute;
    top: 84px; left: 0; width: 100%;
    text-align: center;
    font-family: "Parisienne", cursive;
    font-size: 32px;
    color: var(--cream);
  }

  /* Back: appointment reminder */
  .appointment {
    position: absolute;
    left: 200px; top: 120px;
    font-family: "Dancing Script", cursive;
    font-size: 36px;
    color: var(--ink-soft);
  }
  .appointment h2 {
    margin: 0 0 34px;
    font-weight: 400;
    font-size: 40px;
  }
  .appointment .row {
    display: flex;
    align-items: center;
    height: 60px;
    white-space: nowrap;
  }
  .appointment .check {
    display: inline-block;
    width: 32px; height: 32px;
    margin: 0 26px 0 10px;
    background: var(--box-fill);
    border: 2px solid var(--box-line);
    box-sizing: border-box;
  }
  .appointment .blank {
    display: inline-block;
    border-bottom: 2px solid var(--ink-soft);
    height: 28px;
    margin: 0 10px;
  }
  .appointment .blank--date { width: 190px; }
  .appointment .blank--time { width: 120px; }

  /* Front */
  .band-right {
    position: absolute;
    right: 0; top: 0;
    width: 108px; height: 100%;
    background: var(--band-plum);
  }
  .band-right .disc {
    position: absolute;
    left: 9px; top: 90px;
    width: 90px; height: 90px;
    border-radius: 50%;
    background: var(--disc);
  }
  .name {
    position: absolute;
    left: 250px; top: 56px;
    margin: 0;
    font-family: "Parisienne", cursive;
    font-weight: 400;
    font-size: 52px;
    color: var(--ink);
    white-space: nowrap;
  }
  .name .title {
    font-family: "Dancing Script", cursive;
    font-size: 30px;
  }
  .address {
    position: absolute;
    left: 250px; top: 166px;
    width: 440px;
    margin: 0;
    font-style: normal;
    text-align: center;
    font-family: "Dancing Script", cursive;
    font-size: 29px;
    line-height: 38px;
    color: var(--ink-soft);
  }
  .contacts {
    position: absolute;
    left: 205px; top: 270px;
    margin: 0; padding: 0;
    list-style: none;
    font-family: "Dancing Script", cursive;
    font-size: 30px;
    color: var(--ink-soft);
  }
  .contacts li {
    display: flex;
    align-items: center;
    height: 42px;
    white-space: nowrap;
  }
  .contacts svg {
    width: 31px; height: 27px;
    margin-right: 14px;
    flex: none;
  }
</style>
</head>
<body>
  <div class="card card--back">
    <div class="band-left">
      <div class="brand">Tamsuki</div>
    </div>
    <div class="appointment">
      <h2>Your Next Appointment:</h2>
      <div class="row">
        Mon<span class="check"></span>Tue<span class="check"></span>Wed<span class="check"></span>Thur<span class="check"></span>
      </div>
      <div class="row">
        Date:<span class="blank blank--date"></span>at<span class="blank blank--time"></span>AM<span class="check"></span>PM<span class="check"></span>
      </div>
    </div>
  </div>

  <div class="card card--front">
    <div class="band-left">
      <div class="brand">Tamsuki</div>
    </div>

    <h1 class="name">Velorine Tamsuki <span class="title">DMD</span></h1>

    <address class="address">
      4176 Larchmont Road, Suite D7<br>
      Modesto, CA 95368
    </address>

    <ul class="contacts">
      <li>
        <svg viewBox="0 0 34 30" aria-label="Office">
          <path d="M3 9 Q17 1 31 9 L29 13 L23 11 L23 8 Q17 6 11 8 L11 11 L5 13 Z" fill="var(--ink)"/>
          <path d="M9 14 L25 14 L30 27 L4 27 Z" fill="var(--ink)"/>
          <circle cx="17" cy="20" r="3.5" fill="var(--card)"/>
        </svg>
        209.731.5092
      </li>
      <li>
        <svg viewBox="0 0 34 30" aria-label="Fax">
          <rect x="9" y="2" width="16" height="8" fill="none" stroke="var(--ink)" stroke-width="2.5"/>
          <rect x="2" y="10" width="30" height="12" rx="2" fill="var(--ink)"/>
          <rect x="8" y="18" width="18" height="10" fill="var(--card)" stroke="var(--ink)" stroke-width="2.5"/>
        </svg>
        209.731.8247
      </li>
      <li>
        <svg viewBox="0 0 34 30" aria-label="Email">
          <rect x="3" y="6" width="28" height="19" fill="none" stroke="var(--ink)" stroke-width="2.5"/>
          <path d="M3 6 L17 17 L31 6" fill="none" stroke="var(--ink)" stroke-width="2.5"/>
        </svg>
        tamsukidmd@brivelmail.test
      </li>
    </ul>

    <div class="band-right">
      <div class="disc"></div>
    </div>
  </div>
</body>
</html>
```